Target Market(s)

Corporate

Colors

Designer to choose colors to be used in the design.

Requirements
Must have
• An Overview / Background of the Business & Services- Company Name: ZAKI NURIFOR SMART PROJECTS W prefer as ZAKI NURI. Zaki Nuri offers specialized services in Network information security services, data center & Network infrastructure, data caption & security services, software services. Zaki Nuri provides wide range of services that helps the organization in their business priorities strategies. Zaki Nuri specialized team has handles prestigious projects & executed with ease.
• * The Target Market / Audience you are trying to reach – corporate We are doing CCTV supply & Service, cabling supply & Services , PI system supply & Service, BMS supply & Service, Fire & safety supply & services. we are basically target corporates ,malls, enterprise users and governments.
• * Design Specifics; any preferences or ideas for Style, Colour, Imagery, etc- We prefer mild & unique color.
Nice to have
• Mild and unique color

```html
<!DOCTYPE html>
<html lang="en">
<head>
<meta charset="utf-8">
<title>Zaki Nuri Letterhead</title>
<link href="https://fonts.googleapis.com/css2?family=PT+Sans:wght@400;700&display=swap" rel="stylesheet">
<style>
  :root {
    --backdrop: #d6d6d6;
    --paper: #ffffff;
    --ink: #2b2b2b;
    --ink-soft: #3a3a3a;
    --blue-light: #0aa8e8;
    --blue-dark: #0678b2;
    --footer-dark: #464646;
  }
  * { margin: 0; padding: 0; box-sizing: border-box; }
  html, body { width: 1200px; height: 900px; overflow: hidden; }
  body {
    background: var(--backdrop);
    font-family: "PT Sans", Arial, sans-serif;
    color: var(--ink);
    position: relative;
  }
  .letterhead {
    position: absolute;
    left: 301px;
    top: 65px;
    width: 704px;
    height: 905px;
    background: var(--paper);
    transform: scale(0.857);
    transform-origin: top left;
    overflow: hidden;
  }
  .header-band {
    position: absolute;
    left: 0;
    top: 0;
    width: 704px;
    height: 110px;
    background: linear-gradient(100deg, var(--blue-dark) 0%, var(--blue-light) 55%, var(--blue-light) 100%);
  }
  .footer-band { position: absolute; left: 0; bottom: 0; width: 704px; height: 47px; }
  .footer-band .accent { height: 4px; background: var(--blue-light); }
  .footer-band .base { height: 43px; background: var(--footer-dark); }

  .brand {
    position: absolute;
    left: 440px;
    top: 146px;
    display: flex;
    align-items: center;
    gap: 10px;
  }
  .brand-mark { width: 14px; height: 14px; background: var(--blue-light); }
  .brand-name {
    font-size: 23px;
    font-weight: 700;
    color: var(--ink-soft);
    letter-spacing: 0.3px;
  }

  .recipient { position: absolute; left: 93px; top: 253px; }
  .recipient-name { font-size: 14px; line-height: 17px; }
  .recipient-line { font-size: 9.5px; line-height: 12px; }

  .letter-body {
    position: absolute;
    left: 93px;
    top: 331px;
    width: 546px;
    font-size: 8.7px;
    line-height: 12.35px;
    text-align: justify;
  }
  .letter-body p { margin-bottom: 24.5px; }

  .closing { position: absolute; left: 93px; top: 718px; font-size: 9.5px; }
  .signature {
    position: absolute;
    left: 93px;
    top: 733px;
    width: 88px;
    height: 20px;
    background: linear-gradient(90deg, rgba(43,43,43,0.18), rgba(43,43,43,0.05));
    border-radius: 3px;
  }

  .contact-row {
    position: absolute;
    left: 93px;
    top: 832px;
    width: 548px;
    display: flex;
    justify-content: space-between;
    font-size: 9.5px;
  }
  .contact-item { display: flex; align-items: center; gap: 5px; }
  .contact-item svg { width: 9px; height: 9px; }
</style>
</head>
<body>
  <main class="letterhead">
    <div class="header-band" role="img" aria-label="Decorative blue faceted header pattern"></div>

    <div class="brand">
      <span class="brand-mark"></span>
      <span class="brand-name">ZAKI NURI</span>
    </div>

    <section class="recipient">
      <p class="recipient-name">Mr. Daniel Mercer</p>
      <p class="recipient-line">Managing Director</p>
      <p class="recipient-line">Bright Office Hub</p>
    </section>

    <section class="letter-body">
      <p>Maecenas non rutrum libero. Donec odio lorem, vehicula eu fermentum ut, varius vel purus. Sed varius faucibus enim eu tincidunt. Nullam accumsan metus elit, et blandit risus tincidunt id. Etiam laoreet ultricies est, eu venenatis orci pharetra quis. Cras ut efficitur massa. Mauris nec sodales libero, id pretium quam. Mauris et nulla nec nunc imperdiet ultricies. Sed suscipit, felis eget dignissim luctus, erat nisl euismod nibh, in dignissim nisl est et neque. Proin bibendum quis felis id dignissim. Nulla vitae elementum neque. Nam sollicitudin felis dui, quis consectetur elit accumsan a. Maecenas eget erat eleifend, fermentum metus vel, mattis nunc. Duis at rutrum ligula, sit amet finibus arcu. Aliquam lacus nulla, molestie id porta gravida, rutrum molestie nisi. Proin volutpat nisl ac pharetra dictum. Curabitur sed quam ex. Ut pellentesque pulvinar purus, at sagittis arcu porttitor eu. Nam suscipit vestibulum blandit. Ut tempus ante sed arcu sollicitudin, non hendrerit sem porttitor. In congue in justo ut vehicula. Sed pellentesque felis ut velit placerat, ut tristique massa vestibulum. Integer viverra, massa eget scelerisque tempus, magna quam convallis nibh, vel consectetur turpis diam vitae nisl. Donec lobortis placerat dolor.</p>
      <p>Nullam accumsan metus elit, et blandit risus tincidunt id. Etiam laoreet ultricies est, eu venenatis orci pharetra quis. Cras ut efficitur massa. Mauris nec sodales libero, id pretium quam. Mauris et nulla nec nunc imperdiet ultricies. Sed suscipit, felis eget dignissim luctus, erat nisl euismod nibh, in dignissim nisl est et neque. Proin bibendum quis felis id dignissim. Nulla vitae elementum neque. Nam sollicitudin felis dui, quis consectetur elit accumsan a. Maecenas eget erat eleifend, fermentum metus vel, mattis nunc. Duis at rutrum ligula, sit amet finibus arcu. Aliquam lacus nulla, molestie id porta gravida, rutrum molestie nisi. Proin volutpat nisl ac pharetra dictum. Curabitur sed quam ex accumsan eget erat.</p>
      <p>Nullam accumsan metus elit, et blandit risus tincidunt id. Etiam laoreet ultricies est, eu venenatis orci pharetra quis. Cras ut efficitur massa. Mauris nec sodales libero, id pretium quam. Mauris et nulla nec nunc imperdiet ultricies. Sed suscipit, felis eget dignissim luctus, erat nisl euismod nibh, in dignissim nisl est et neque. Proin bibendum quis felis id dignissim. Nulla vitae elementum neque. Nam sollicitudin felis dui, quis consectetur elit accumsan.</p>
    </section>

    <p class="closing">Sincerely</p>
    <div class="signature" role="img" aria-label="Handwritten signature of the sender"></div>

    <footer class="contact-row">
      <span class="contact-item">
        <svg viewBox="0 0 10 10" aria-hidden="true"><path d="M2 1 L4 1 L4.6 3 L3.5 4 Q4.5 6 6 6.5 L7 5.4 L9 6 L9 8 Q8 9 6.5 8.6 Q2.5 7.5 1.2 3.4 Q1 2 2 1 Z" fill="var(--blue-light)"/></svg>
        88-456-210734
      </span>
      <span class="contact-item">
        <svg viewBox="0 0 10 10" aria-hidden="true"><circle cx="5" cy="5" r="5" fill="var(--blue-light)"/><rect x="2.4" y="3.3" width="5.2" height="3.6" fill="#fff"/><path d="M2.4 3.3 L5 5.3 L7.6 3.3" stroke="var(--blue-light)" stroke-width="0.7" fill="none"/></svg>
        northline@email.com
      </span>
      <span class="contact-item">
        <svg viewBox="0 0 10 10" aria-hidden="true"><circle cx="5" cy="5" r="4.4" fill="none" stroke="var(--blue-light)" stroke-width="0.9"/><ellipse cx="5" cy="5" rx="1.8" ry="4.4" fill="none" stroke="var(--blue-light)" stroke-width="0.8"/><line x1="0.6" y1="5" x2="9.4" y2="5" stroke="var(--blue-light)" stroke-width="0.8"/></svg>
        www.northline.com
      </span>
      <span class="contact-item">
        <svg viewBox="0 0 10 10" aria-hidden="true"><circle cx="5" cy="5" r="5" fill="var(--blue-light)"/><path d="M5 2 C3.6 2 2.8 3 2.8 4.1 C2.8 5.6 5 8 5 8 C5 8 7.2 5.6 7.2 4.1 C7.2 3 6.4 2 5 2 Z" fill="#fff"/><circle cx="5" cy="4.1" r="0.8" fill="var(--blue-light)"/></svg>
        42 Maple Lane, Dunvale, Canada K412
      </span>
    </footer>

    <div class="footer-band">
      <div class="accent"></div>
      <div class="base"></div>
    </div>
  </main>
</body>
</html>
```